Business Card design for Accounting and Consulting Firm
R.T. BALLISTER HOLDINGS, LLC
Business Card design for Accounting and Consulting Firm - Financial Services
Creative Brief
Use same font as used in my logo
trajan bold
Professional
Nell Whitcombe
President
I do not want address on the card
nwhitcombe@rtballister-example.com
www.rtballister-example.com
CFO Advisory / Bookkeeping Plinwor Ledgerly Consulting
either logo without text or logo with text whichever is not used on the front of card.
rtballister rtballister
You can use other fonts, I just listed the one that is used in the text with the logo so you would know what that is. Pantone Hex Colors used: BLUE #012377 (C:96 - M:77 - Y:14 - K:4) #021856 (C:96 - M:82 - Y:28 - K:16) #095CD3 (C:95 - M:47 - Y:0 - K:0) Gold #987412 (C:29 - M:37 - Y:91 - K:16) #E4BB2C (C:9 - M:23 - Y:82 - K:1)

```html
<!DOCTYPE html>
<html lang="en">
<head>
<meta charset="utf-8">
<title>R.T. Ballister Holdings, LLC — Business Card</title>
<link href="https://fonts.googleapis.com/css2?family=Cinzel:wght@400;600;700&display=swap" rel="stylesheet">
<style>
  :root {
    --blue-deep: #012377;
    --blue-navy: #021856;
    --blue-bright: #095CD3;
    --gold-dark: #987412;
    --gold-light: #E4BB2C;
    --paper: #ffffff;
    --backdrop: #e9e7e3;
  }
  * { box-sizing: border-box; margin: 0; padding: 0; }
  html, body {
    width: 1200px; height: 891px; overflow: hidden;
    background: var(--backdrop);
    font-family: "Cinzel", serif;
  }
  .sheet {
    position: relative; width: 1200px; height: 891px;
    display: flex; flex-direction: column; align-items: center; justify-content: center; gap: 36px;
  }
  .card {
    position: relative; width: 660px; height: 377px;
    background: var(--paper); border-radius: 22px; overflow: hidden;
    box-shadow: 0 10px 28px rgba(0,0,0,.18);
  }

  /* Front */
  .brand {
    position: absolute; left: 0; right: 0; top: 110px;
    display: flex; align-items: center; justify-content: center; gap: 22px;
  }
  .brand-dot { width: 74px; height: 74px; border-radius: 50%; background: var(--blue-deep); }
  .brand-name {
    color: var(--blue-deep); font-weight: 700; font-size: 34px; line-height: 1.05; letter-spacing: .02em;
  }
  .brand-rule {
    position: absolute; left: 190px; right: 60px; top: 214px; height: 3px;
    background: linear-gradient(90deg, var(--gold-light), var(--gold-dark));
  }
  .services {
    position: absolute; left: 0; right: 0; top: 246px;
    display: flex; justify-content: center; gap: 44px; list-style: none;
    color: var(--blue-navy); font-size: 14px; font-weight: 600;
  }
  .services li { display: flex; align-items: center; gap: 7px; }
  .services svg { width: 15px; height: 15px; }

  /* Back */
  .contact {
    position: absolute; left: 46px; top: 58px; list-style: none;
    color: var(--blue-navy); font-size: 14px; font-weight: 600;
  }
  .contact li { display: flex; align-items: center; gap: 12px; height: 30px; }
  .contact .icon {
    width: 20px; height: 20px; border-radius: 50%; background: var(--gold-dark);
    display: flex; align-items: center; justify-content: center;
  }
  .contact .icon svg { width: 12px; height: 12px; }
  .person {
    position: absolute; right: 58px; top: 74px; text-align: right;
  }
  .person-name { color: var(--blue-deep); font-size: 34px; font-weight: 700; letter-spacing: .02em; }
  .person-rule { height: 2px; margin: 6px 0 6px 40px; background: linear-gradient(90deg, var(--gold-light), var(--gold-dark)); }
  .person-title { color: var(--gold-dark); font-size: 18px; font-weight: 600; letter-spacing: .12em; }
  .wave { position: absolute; left: 0; bottom: 0; width: 660px; height: 377px; }
</style>
</head>
<body>
<main class="sheet">

  <section class="card card-front" aria-label="Card front">
    <div class="brand">
      <span class="brand-dot"></span>
      <div class="brand-name">R.T. BALLISTER<br>HOLDINGS, LLC</div>
    </div>
    <div class="brand-rule"></div>
    <ul class="services">
      <li><svg viewBox="0 0 16 16"><path d="M2 9l4 4 8-10" fill="none" stroke="#987412" stroke-width="2.4" stroke-linecap="round"/></svg>CFO Advisory</li>
      <li><svg viewBox="0 0 16 16"><path d="M2 9l4 4 8-10" fill="none" stroke="#987412" stroke-width="2.4" stroke-linecap="round"/></svg>Bookkeeping</li>
      <li><svg viewBox="0 0 16 16"><path d="M2 9l4 4 8-10" fill="none" stroke="#987412" stroke-width="2.4" stroke-linecap="round"/></svg>Plinwor Ledgerly Consulting</li>
    </ul>
  </section>

  <section class="card card-back" aria-label="Card back">
    <ul class="contact">
      <li><span class="icon"><svg viewBox="0 0 12 12"><path d="M3 1h2l1 3-1.5 1a6 6 0 0 0 2.5 2.5L8 6l3 1v2c0 1-1 2-2 2A9 9 0 0 1 1 3c0-1 1-2 2-2z" fill="#fff"/></svg></span>555.014.2231</li>
      <li><span class="icon"><svg viewBox="0 0 12 12"><rect x="3" y="1" width="6" height="10" rx="1" fill="#fff"/></svg></span>555.017.4408</li>
      <li><span class="icon"><svg viewBox="0 0 12 12"><rect x="2" y="4" width="8" height="5" fill="#fff"/><rect x="3.5" y="1.5" width="5" height="3" fill="#fff"/></svg></span>555.019.6652</li>
      <li><span class="icon"><svg viewBox="0 0 12 12"><rect x="1" y="3" width="10" height="7" fill="#fff"/><path d="M1 3l5 4 5-4" fill="none" stroke="#987412" stroke-width="1"/></svg></span>nwhitcombe@rtballister-example.com</li>
      <li><span class="icon"><svg viewBox="0 0 12 12"><circle cx="6" cy="6" r="4.5" fill="none" stroke="#fff" stroke-width="1.2"/><path d="M1.5 6h9M6 1.5c2 2 2 7 0 9M6 1.5c-2 2-2 7 0 9" fill="none" stroke="#fff" stroke-width="1"/></svg></span>www.rtballister-example.com</li>
    </ul>
    <div class="person">
      <div class="person-name">NELL WHITCOMBE</div>
      <div class="person-rule"></div>
      <div class="person-title">PRESIDENT</div>
    </div>
    <svg class="wave" viewBox="0 0 660 377" aria-hidden="true">
      <defs>
        <linearGradient id="blueSweep" x1="0" y1="0" x2="1" y2="1">
          <stop offset="0" stop-color="#095CD3"/>
          <stop offset="1" stop-color="#012377"/>
        </linearGradient>
        <linearGradient id="goldSweep" x1="0" y1="0" x2="1" y2="0">
          <stop offset="0" stop-color="#E4BB2C"/>
          <stop offset="1" stop-color="#987412"/>
        </linearGradient>
      </defs>
      <path d="M150 377 C330 300 500 270 660 240 L660 377 Z" fill="url(#blueSweep)"/>
      <path d="M0 300 C220 345 440 290 660 228 L660 240 C440 300 220 356 0 312 Z" fill="url(#goldSweep)"/>
    </svg>
  </section>

</main>
</body>
</html>
```